Business Card Design - Furniture Retail

Open to both Single or double sided design

We are launching a online ecommerce store that sells Scandinavian/Danish style of furniture in Australia.

We aspire to provide stylish but classic and designers' selection of furniture to the Australia public at affordable price. For the style of the furniture we are selling, please see the following links:

https://www.filecrate.example/sh/qk3mzr8wlp/BXTpLnR4vQ7cYdHs?dl=0

The style of the design we are looking for is clean, simple that look Scandinavian/Danish but yet it is timeless classic.

Aspiring Design
http://www.lindmora.com
http://tobyquell.com.au/
http://vekt.furniture/
http://www.olvo.com/
Updates

Please display the card on normal angle for both front and back instead of funny angle. Please keep it display when displaying the design of the business cards so that we can focus on the designs rather than being confused by the unnecessary stuffs like the hands or background

I think there is already enough curve line on the logo itself so anything extra of the curve on the business card would be really unnecessary. Please avoid using any of the extra curve line on the business card, other than the logo itself. Thanks

Regular card and give them a matt celloglaze to create texture on card that makes it looked luxury and expensive.

Please display design on normal angle! Please only use white colour in the background (not the business card but the referring to the submission) rather than anything fancy so that we can focus on the design.

Target Market(s)

High end market consumers who are financially capable and who has good taste and appreciate good design

aged between 28 - 45 white collars professional/businessmen who live in metropolitan areas

Industry/Entity Type

Business

Font styles to use
Serif
Sans Serif

Requirements
Must have
• Regular card and give them a matt celloglaze to create texture on card that makes it looked luxury and expensive.

Please use the logo from the uploaded files

Company Name: Milo Verhagen
Name: Milo Reeb
Phone: +614 27 305 641
Website: www.miloverhagen.com.au
Email: milo@miloverhagen.com.au
Nice to have
• Colour is not limited to black and white
Should not have
• The concept photos of the furniture should NOT be used in the FRONT page of the business card.

```html
<!DOCTYPE html>
<html lang="en">
<head>
<meta charset="utf-8">
<title>Milo Verhagen — Business Card</title>
<link href="https://fonts.googleapis.com/css2?family=Bitter:wght@400&family=Roboto:wght@400&display=swap" rel="stylesheet">
<style>
  :root {
    --page: #ffffff;
    --card-black: #0f0f10;
    --mark-gloss: #242426;
    --card-white: #f7f7f5;
    --card-edge: #e2e2e0;
    --ink: #1c1c1c;
    --label: #9a9a9a;
    --serif: "Bitter", Georgia, serif;
    --sans: "Roboto", Arial, sans-serif;
  }
  * { margin: 0; padding: 0; box-sizing: border-box; }
  html, body {
    width: 1200px;
    height: 900px;
    overflow: hidden;
    background: var(--page);
  }
  .sheet {
    position: relative;
    width: 1200px;
    height: 900px;
    display: flex;
    align-items: center;
    justify-content: center;
    gap: 60px;
  }
  .card {
    position: relative;
    width: 480px;
    height: 292px;
    border-radius: 2px;
    box-shadow: 0 10px 28px rgba(0, 0, 0, 0.10), 0 2px 6px rgba(0, 0, 0, 0.06);
  }
  .card--front {
    background: var(--card-black);
    display: flex;
    align-items: center;
    justify-content: center;
  }
  .brand-name {
    font-family: var(--serif);
    font-weight: 400;
    font-size: 30px;
    letter-spacing: 0.18em;
    text-transform: uppercase;
    color: var(--mark-gloss);
  }
  .card--back {
    background: var(--card-white);
    border: 1px solid var(--card-edge);
  }
  .contact {
    position: absolute;
    left: 58px;
    top: 150px;
  }
  .contact__name {
    font-family: var(--serif);
    font-size: 19px;
    color: var(--ink);
    margin-bottom: 8px;
  }
  .contact__row {
    display: flex;
    align-items: baseline;
    line-height: 19px;
  }
  .contact__label {
    width: 58px;
    font-family: var(--sans);
    font-size: 9px;
    letter-spacing: 0.06em;
    text-transform: uppercase;
    color: var(--label);
  }
  .contact__value {
    font-family: var(--serif);
    font-size: 13px;
    color: var(--ink);
  }
</style>
</head>
<body>
  <main class="sheet">
    <section class="card card--front" aria-label="Card front">
      <span class="brand-name">Milo Verhagen</span>
    </section>
    <section class="card card--back" aria-label="Card back">
      <div class="contact">
        <p class="contact__name">Milo Reeb</p>
        <p class="contact__row"><span class="contact__label">Phone</span><span class="contact__value">+614 27 305 641</span></p>
        <p class="contact__row"><span class="contact__label">E-mail</span><span class="contact__value">milo@miloverhagen.com.au</span></p>
        <p class="contact__row"><span class="contact__label">Web</span><span class="contact__value">www.miloverhagen.com.au</span></p>
      </div>
    </section>
  </main>
</body>
</html>
```